Graphic Design/Logo Needed for Ear Drops Bottle

We have an Ear Drop Medication that we need to create a new label for. We will use a retro picture of a Doctor (Dr. Halvane) and the name of the product is Mighty Lobe. There is no official logo, so we will want to create a retro, basic logo for Mighty Lobe and use the retro picture. Front portion of the label is Size is 1.5" in height, and about 1.375" Width. this is a small tube similar in size to eye drops. We will be looking for just the logo portion and what you will see on the front of the bottle.

Target Market(s)

Medical Container

Industry/Entity Type

Medical

Font styles to use
Serif
Sans Serif

Colors
0054AA
0677BA
7BADD7
CADEEF
E8F1F8
FFF300
FFF600
FEFA6F
FFFEC7
FFFEE8

Requirements
Must have
• Picture of Dr. Halvane, "Mighty Lobe", Dr. Halvane's Ear Solution
Nice to have
• Retro Style or Modern with Retro Feel, Clean and engaging

```html
<!DOCTYPE html>
<html lang="en">
<head>
<meta charset="utf-8">
<title>Mighty Lobe – Dr. Halvane's Ear Solution Label</title>
<link href="https://fonts.googleapis.com/css2?family=Oswald:wght@500;700&family=Pinyon+Script&family=Old+Standard+TT&display=swap" rel="stylesheet">
<style>
  :root {
    --page: #f2f2f2;
    --label: #ece7da;
    --ink: #1f1f1f;
    --ink-soft: rgba(40, 40, 40, 0.28);
    --ink-faint: rgba(40, 40, 40, 0.18);
    --band-text: #f4f1ea;
    --photo-light: #d9d5cc;
    --photo-dark: #6f6c67;
  }
  * { margin: 0; padding: 0; box-sizing: border-box; }
  html, body { width: 1200px; height: 1200px; overflow: hidden; background: var(--page); }
  .canvas { position: relative; width: 1200px; height: 1200px; }
  .label {
    position: absolute; left: 220px; top: 130px; width: 760px; height: 940px;
    background: var(--label); border-radius: 6px; overflow: hidden;
    box-shadow: 0 2px 12px rgba(0,0,0,0.06);
  }
  .faint-copy {
    position: absolute; font-family: "Old Standard TT", serif;
    color: var(--ink-faint); font-size: 17px; line-height: 1.55;
  }
  .faint-copy.left-column { left: 34px; top: 110px; width: 150px; }
  .faint-copy.left-column p + p { margin-top: 36px; }
  .faint-copy.right-top { left: 470px; top: 48px; width: 250px; font-style: italic; }
  .portrait {
    position: absolute; left: 195px; top: 95px; width: 380px; height: 470px;
    border-radius: 46% 46% 8px 8px / 30% 30% 8px 8px;
    background: radial-gradient(ellipse at 50% 38%, var(--photo-light) 0%, #a9a59d 45%, var(--photo-dark) 100%);
    opacity: 0.85;
  }
  .script-name {
    position: absolute; left: 520px; top: 250px; width: 230px;
    font-family: "Pinyon Script", cursive; font-size: 52px; line-height: 0.95;
    color: var(--ink-soft); transform: rotate(-14deg); text-align: center;
  }
  .practice-name {
    position: absolute; left: 560px; top: 430px; width: 190px;
    font-family: "Old Standard TT", serif; color: var(--ink-soft);
    font-size: 27px; line-height: 1.05;
  }
  .practice-name small { display: block; font-size: 12px; margin-bottom: 4px; }
  .title { position: absolute; left: 0; top: 500px; width: 760px; height: 300px; }
  .title text { font-family: "Oswald", sans-serif; font-weight: 700; fill: var(--ink); }
  .title .maker-tag { font-weight: 500; fill: var(--ink-faint); font-size: 14px; letter-spacing: 1px; }
  .title .rule { stroke: var(--ink); stroke-width: 3; }
  .product-band {
    position: absolute; left: 120px; top: 818px; width: 520px; height: 54px;
    background: var(--ink); color: var(--band-text);
    font-family: "Oswald", sans-serif; font-weight: 500; font-size: 29px;
    letter-spacing: 2px; text-align: center; line-height: 54px; text-transform: uppercase;
  }
</style>
</head>
<body>
<div class="canvas">
  <div class="label">
    <div class="faint-copy left-column">
      <p>Dr. Halvane has provided expert ear care to local families for decades.</p>
      <p>Dr. Halvane will provide diagnosis and treatment for hearing, sinus and allergy conditions.</p>
    </div>
    <div class="faint-copy right-top">A trusted name in ear, nose and throat care since the early days.</div>

    <div class="portrait" role="img" aria-label="Retro black and white photograph of Dr. Halvane wearing a head mirror and white coat"></div>

    <div class="script-name">Dr. Halvane's</div>
    <div class="practice-name"><small>Established practice</small>Ear Nose &amp; Throat Physicians</div>

    <svg class="title" viewBox="0 0 760 300" aria-label="Mighty Lobe">
      <defs>
        <path id="title-arc" d="M70 170 Q380 60 690 170"/>
      </defs>
      <text font-size="150" text-anchor="middle">
        <textPath href="#title-arc" startOffset="50%" textLength="600" lengthAdjust="spacingAndGlyphs">MIGHTY</textPath>
      </text>
      <line class="rule" x1="220" y1="238" x2="290" y2="238"/>
      <line class="rule" x1="232" y1="250" x2="290" y2="250"/>
      <line class="rule" x1="470" y1="238" x2="540" y2="238"/>
      <line class="rule" x1="470" y1="250" x2="528" y2="250"/>
      <text x="380" y="290" font-size="96" text-anchor="middle">LOBE</text>
      <text class="maker-tag" x="495" y="222">DR. HALVANE</text>
    </svg>

    <div class="product-band">Dr. Halvane's Ear Solution</div>
  </div>
</div>
</body>
</html>
```